Blog Design for Meridian Dispatch

Need a very simple blog template (see attachment, Frontpage) that includes entries and ability to upload photos/video. Tabs are not needed (See Tobin Bistro Moderne blog for sort of what I am going for but a lot less cluttered). A section that can access old entries is needed as well as a "contact me" tab. The format should be very simple. An entry and section for comments, new entry, section for comments etc. comments sections should be able to be monitored by me. With the ability for readers to contribute via coinlark. The look and feel should be sophisticated and should target an educated global audience. The blog is all about commenting on global news around the world. For example, a news article could be photographed and then commented on. Type face should be simple, clean and 1930's style. See Brisk Ledger magazine for looks and feel. If viewers wish to contribute they can make donations via coinlark on the site. Once the template is competed it should be very easy for me to update and work with and handed over to a web hosting service. I own the domain name which I want to use. It would be best to use an existing template eg wordpress. So in simple terms need a wordpress template adapted for this blog idea. Not sure what coded vs. uncoded means. But the overall objective is very simple. Template should be clean, no design elements other than the name of the blog.

Target Market(s)

Educated people from around the world interested in current events

Industry/Entity Type

News

Number of Pages Required

2 page

Other font styles liked:
• Upper East Side

Colors
0255a3
1b1b1b
5c5c5c

Requirements
Must have
• This is a blog so it should have all the standard features including daily updates, photo/video upload, comments that can be monitored by me, coinlark donation link. It should be easy for me to use and handle once completed and delivered to web host. It must have a simple, elegant look and feel. I have chose Serif font style but recommend a 1930's Art Deco - clean, unfussy type face. Type face Upper East Side is what I am looking for
Nice to have
• The look must be simple and no pictures, design elements or logos. Clean and crisp
Should not have
• Any pictures for illustrations as part of the overall design

```html
<!DOCTYPE html>
<html lang="en">
<head>
<meta charset="utf-8">
<title>Meridian Dispatch</title>
<link rel="stylesheet" href="https://fonts.googleapis.com/css2?family=Open+Sans:wght@400;600;700&family=PT+Sans+Narrow:wght@400;700&display=swap">
<style>
:root{
  --blue:#0255a3;
  --ink:#1b1b1b;
  --grey:#5c5c5c;
  --light:#f1efef;
  --rule:#dcdcdc;
  --footer:#1f1f1f;
  --white:#ffffff;
}
*{box-sizing:border-box;margin:0;padding:0}
html,body{width:1200px;height:2584px;overflow:hidden;background:var(--white);font-family:"Open Sans",sans-serif;color:var(--grey)}
.page{position:relative;width:1200px;height:2584px}
.topline{height:6px;background:var(--blue)}
.header{position:relative;height:94px;width:708px;margin:0 auto}
.brand{position:absolute;left:0;top:48px;font-family:"Open Sans",sans-serif;font-weight:700;font-size:20px;color:var(--blue)}
.social-top{position:absolute;right:0;top:10px;display:flex;gap:6px}
.dot{width:12px;height:12px;border-radius:50%;background:var(--blue)}
.nav{position:absolute;right:0;top:54px;display:flex;align-items:center;gap:22px;font-size:10px;font-weight:600;color:var(--ink);text-transform:uppercase}
.nav .active{color:var(--blue)}
.nav .login{border:1px solid var(--blue);color:var(--blue);padding:3px 12px;border-radius:2px}
.header-rule{height:1px;background:var(--rule)}
.hero{position:relative;height:300px;background:linear-gradient(180deg,#3a3431 0%,#5a4f48 45%,#2c2724 100%);display:flex;flex-direction:column;align-items:center;justify-content:center;color:var(--white);text-align:center}
.hero h1{font-weight:600;font-size:30px}
.hero p{font-size:11px;margin-top:8px;max-width:520px;opacity:.9}
.hero .btn{margin-top:16px;border:1px solid var(--white);font-size:10px;padding:5px 16px;background:rgba(0,0,0,.35)}
.content{width:708px;margin:22px auto 0;display:flex;justify-content:space-between}
.main{width:408px}
.post{border-bottom:1px solid var(--rule);padding-bottom:26px;margin-bottom:22px}
.post h2{font-family:"PT Sans Narrow",sans-serif;font-weight:700;font-size:18px;line-height:21px;color:var(--ink)}
.meta{display:flex;align-items:center;font-size:9px;margin:16px 0 14px;color:var(--grey)}
.meta svg{margin-right:5px}
.meta .gap{width:30px}
.shares{margin-left:auto;display:flex;gap:6px}
.shares span{width:9px;height:9px;background:var(--ink)}
.photo{width:100%;display:flex;align-items:center;justify-content:center}
.excerpt{font-size:9px;line-height:14px;margin-top:12px}
.more{display:inline-block;margin-top:14px;background:var(--blue);color:var(--white);font-size:10px;font-weight:600;padding:5px 18px}
.sidebar{width:228px}
.box{background:var(--light);padding:12px 12px 14px;margin-bottom:14px}
.box h3{font-size:10px;font-weight:700;color:var(--ink);text-transform:uppercase;margin-bottom:8px}
.box p{font-size:8.5px;line-height:13px}
.box .more{margin:12px auto 0;display:block;width:90px;text-align:center;font-size:9px;padding:4px 0}
.tabs{display:flex;justify-content:space-between;font-size:9px;font-weight:600;color:var(--ink);padding:0 6px 6px;border-bottom:1px solid var(--rule);margin-bottom:8px}
.item{display:flex;gap:8px;margin-bottom:8px}
.thumb{width:44px;height:36px;flex:none}
.item b{display:block;font-size:8.5px;line-height:11px;color:var(--ink)}
.item small{font-size:7.5px}
.stream{height:120px;display:grid;grid-template-columns:2fr 1fr;gap:3px}
.field{background:var(--white);border:1px solid var(--rule);height:18px;font-size:8px;padding:3px 6px;margin-bottom:6px;color:#999}
.submit{background:var(--blue);color:var(--white);text-align:center;font-size:9px;height:18px;line-height:18px}
.note{font-size:8.5px;line-height:13px;margin-bottom:10px}
.note a{color:var(--blue);text-decoration:none;display:block}
.footer{position:absolute;left:0;bottom:0;width:1200px;height:44px;background:var(--footer);color:#cfcfcf;font-size:9px}
.footer .inner{width:708px;margin:0 auto;height:44px;display:flex;align-items:center;justify-content:space-between}
.footer .dots{display:flex;gap:6px}
.footer .dot{background:none;border:1px solid #cfcfcf}
</style>
</head>
<body>
<div class="page">
  <div class="topline"></div>
  <header class="header">
    <div class="brand">Meridian Dispatch</div>
    <div class="social-top"><span class="dot"></span><span class="dot"></span><span class="dot"></span><span class="dot"></span><span class="dot"></span><span class="dot"></span></div>
    <nav class="nav"><span class="active">Home</span><span>About Us</span><span>Our Products</span><span>News</span><span>Contact</span><span class="login">Login</span></nav>
  </header>
  <div class="header-rule"></div>
  <section class="hero" role="img" aria-label="Dark photograph of large stacked letters on a wooden surface">
    <h1>Lorem ipsum dolor sit amet, consectetur</h1>
    <p>Nullam et mauris dui. Interdum et malesuada fames ac ante ipsum primis in faucibus sed</p>
    <span class="btn">Learn More</span>
  </section>

  <div class="content">
    <main class="main">
      <article class="post">
        <h2>Lorem ipsum dolor sit amet, consectetur adipiscing elit. Nullam et mauris dui. Interdum et Morb</h2>
        <div class="meta"><svg width="9" height="9" viewBox="0 0 10 10"><circle cx="5" cy="3" r="2.5" fill="#5c5c5c"/><path d="M0 10a5 4 0 0 1 10 0z" fill="#5c5c5c"/></svg>Lorem Ipsum Dolor<span class="gap"></span><svg width="9" height="9" viewBox="0 0 10 10"><rect x=".5" y="1.5" width="9" height="8" fill="none" stroke="#5c5c5c"/><rect x=".5" y="1.5" width="9" height="2" fill="#5c5c5c"/></svg>28 February 2015<div class="shares"><span></span><span></span><span></span><span></span><span></span></div></div>
        <div class="photo" role="img" aria-label="Black and white photo of a folded newspaper" style="height:204px;background:linear-gradient(135deg,#e4e4e4,#8a8a8a 60%,#3d3d3d)"></div>
        <p class="excerpt">Nullam et mauris dui. Interdum et malesuada fames ac ante ipsum primis in faucibus. Morbi sed sem et nisl tempor pretium eget quis arcu vitae.</p>
        <span class="more">Read More</span>
      </article>
      <article class="post">
        <h2>Lorem ipsum dolor sit amet, consectetur adipiscing elit. Nullam et mauris dui. Interdum et Morb</h2>
        <div class="meta"><svg width="9" height="9" viewBox="0 0 10 10"><circle cx="5" cy="3" r="2.5" fill="#5c5c5c"/><path d="M0 10a5 4 0 0 1 10 0z" fill="#5c5c5c"/></svg>Lorem Ipsum Dolor<span class="gap"></span><svg width="9" height="9" viewBox="0 0 10 10"><rect x=".5" y="1.5" width="9" height="8" fill="none" stroke="#5c5c5c"/><rect x=".5" y="1.5" width="9" height="2" fill="#5c5c5c"/></svg>28 February 2015<div class="shares"><span></span><span></span><span></span><span></span><span></span></div></div>
        <div class="photo" role="img" aria-label="Video still of a microphone in a dark studio" style="height:212px;background:radial-gradient(circle at 50% 50%,#6b6b6b,#1e1e1e 75%)">
          <svg width="46" height="46" viewBox="0 0 46 46"><circle cx="23" cy="23" r="21" fill="rgba(0,0,0,.45)" stroke="#fff" stroke-width="2"/><path d="M18 14l14 9-14 9z" fill="#fff"/></svg>
        </div>
        <p class="excerpt">Nullam et mauris dui. Interdum et malesuada fames ac ante ipsum primis in faucibus. Morbi sed sem et nisl tempor pretium eget quis arcu vitae.</p>
        <span class="more">Read More</span>
      </article>
      <article class="post">
        <h2>Lorem ipsum dolor sit amet, consectetur adipiscing elit. Nullam et mauris dui. Interdum et Morb</h2>
        <div class="meta"><svg width="9" height="9" viewBox="0 0 10 10"><circle cx="5" cy="3" r="2.5" fill="#5c5c5c"/><path d="M0 10a5 4 0 0 1 10 0z" fill="#5c5c5c"/></svg>Lorem Ipsum Dolor<span class="gap"></span><svg width="9" height="9" viewBox="0 0 10 10"><rect x=".5" y="1.5" width="9" height="8" fill="none" stroke="#5c5c5c"/><rect x=".5" y="1.5" width="9" height="2" fill="#5c5c5c"/></svg>28 February 2015<div class="shares"><span></span><span></span><span></span><span></span><span></span></div></div>
        <div class="photo" role="img" aria-label="Stack of newspapers seen from the side" style="height:212px;background:linear-gradient(160deg,#f2f2f2,#b9b9b9 50%,#6e6e6e)"></div>
        <p class="excerpt">Nullam et mauris dui. Interdum et malesuada fames ac ante ipsum primis in faucibus. Morbi sed sem et nisl tempor pretium eget quis arcu vitae.</p>
        <span class="more">Read More</span>
      </article>
      <article class="post">
        <h2>Lorem ipsum dolor sit amet, consectetur adipiscing elit. Nullam et mauris dui. Interdum et Morb</h2>
        <div class="meta"><svg width="9" height="9" viewBox="0 0 10 10"><circle cx="5" cy="3" r="2.5" fill="#5c5c5c"/><path d="M0 10a5 4 0 0 1 10 0z" fill="#5c5c5c"/></svg>Lorem Ipsum Dolor<span class="gap"></span><svg width="9" height="9" viewBox="0 0 10 10"><rect x=".5" y="1.5" width="9" height="8" fill="none" stroke="#5c5c5c"/><rect x=".5" y="1.5" width="9" height="2" fill="#5c5c5c"/></svg>28 February 2015<div class="shares"><span></span><span></span><span></span><span></span><span></span></div></div>
        <div class="photo" role="img" aria-label="Fanned pile of colourful magazines" style="height:232px;background:linear-gradient(150deg,#d8dde3,#7d8894 50%,#3e4650)"></div>
        <p class="excerpt">Nullam et mauris dui. Interdum et malesuada fames ac ante ipsum primis in faucibus. Morbi sed sem et nisl tempor pretium eget quis arcu vitae.</p>
        <span class="more">Read More</span>
      </article>
      <article class="post" style="border:none">
        <h2>Lorem ipsum dolor sit amet, consectetur adipiscing elit. Nullam et mauris dui. Interdum et Morb</h2>
        <div class="meta"><svg width="9" height="9" viewBox="0 0 10 10"><circle cx="5" cy="3" r="2.5" fill="#5c5c5c"/><path d="M0 10a5 4 0 0 1 10 0z" fill="#5c5c5c"/></svg>Lorem Ipsum Dolor<span class="gap"></span><svg width="9" height="9" viewBox="0 0 10 10"><rect x=".5" y="1.5" width="9" height="8" fill="none" stroke="#5c5c5c"/><rect x=".5" y="1.5" width="9" height="2" fill="#5c5c5c"/></svg>28 February 2015<div class="shares"><span></span><span></span><span></span><span></span><span></span></div></div>
        <div class="photo" role="img" aria-label="Black and white photo of a reporter's microphone" style="height:228px;background:radial-gradient(circle at 50% 55%,#7a7a7a,#e9e9e9 65%)"></div>
      </article>
    </main>

    <aside class="sidebar">
      <section class="box">
        <h3>About Us</h3>
        <p>Lorem ipsum dolor sit amet, consectetur adipiscing elit. Nullam et mauris dui. Interdum et malesuada fames ac ante ipsum primis in faucibus. Morbi sed sem et nisl tempor pretium eget.</p>
        <span class="more">Read More</span>
      </section>
      <section class="box" style="height:208px">
        <div class="tabs"><span>Recent</span><span>Popular</span><span>Tags</span></div>
        <div class="item"><div class="thumb" role="img" aria-label="Newspaper thumbnail" style="background:linear-gradient(135deg,#ddd,#777)"></div><div><b>Pellentesque habitant morbi tristique</b><small>28 February 2015</small></div></div>
        <div class="item"><div class="thumb" role="img" aria-label="Magazines thumbnail" style="background:linear-gradient(135deg,#d9c7a8,#7a6a55)"></div><div><b>Pellentesque habitant morbi tristique</b><small>28 February 2015</small></div></div>
        <div class="item"><div class="thumb" role="img" aria-label="Newspaper stack thumbnail" style="background:linear-gradient(135deg,#eee,#8c8c8c)"></div><div><b>Pellentesque habitant morbi tristique</b><small>28 February 2015</small></div></div>
      </section>
      <section class="box" style="background:none;padding:6px 0;border-top:1px solid var(--rule)">
        <h3>Photo Stream</h3>
        <div class="stream">
          <div role="img" aria-label="Newspaper and coffee cup photo" style="grid-row:span 2;background:linear-gradient(135deg,#f0f0f0,#9a9a9a)"></div>
          <div role="img" aria-label="Small news photo" style="background:linear-gradient(135deg,#ccc,#555)"></div>
          <div role="img" aria-label="Small news photo" style="background:linear-gradient(135deg,#bbb,#444)"></div>
        </div>
      </section>
      <section class="box">
        <h3>Newsletter</h3>
        <div class="field">Name</div>
        <div class="field">Email ID</div>
        <div class="field">Country</div>
        <div class="submit">Submit</div>
      </section>
      <section class="box">
        <h3>Short Notes</h3>
        <div class="note">Lorem ipsum dolor sit amet, consectetur adipiscing elit nullam et mauris.<a>#worldwatch</a></div>
        <div class="note">Interdum et malesuada fames ac ante ipsum primis in faucibus morbi.<a>#dailyview</a></div>
      </section>
    </aside>
  </div>

  <footer class="footer">
    <div class="inner"><span>Copyright © 2015 Meridian Dispatch</span><div class="dots"><span class="dot"></span><span class="dot"></span><span class="dot"></span><span class="dot"></span><span class="dot"></span><span class="dot"></span></div></div>
  </footer>
</div>
</body>
</html>
```